Update the A4 Specials Page for Restaurant/Cafe

Provide a MINIMALIST attractive Specials page we can print weekly for our food and drink specials to give to our guests. Final design is to be provided in WORD Document so it can be easily edited by Manager. Should be black text and MINIMALIST to minimise ink usage as we print hundreds a week. We have UPLOADED the existing page as a template for you to update. Maybe logo can stay, see what you think. Or delete it and do something else. Keep it simple. Choose a good FONT. Could be a little playful with a cocktail ICON or something. Our existing menus can be seen at www.tallowmillcafe.com.au and they are using font Alegreya. Please note we are unable to provide any feedback to designers, however we really do appreciate your time if you are submitting a design. Thank you for your participation.

```html
<!DOCTYPE html>
<html lang="en">
<head>
<meta charset="utf-8">
<title>Tallow Mill Cafe – Weekly Specials</title>
<link href="https://fonts.googleapis.com/css2?family=Alegreya:ital,wght@0,400;0,900&display=swap" rel="stylesheet">
<style>
  :root {
    --ink: #2f5a63;
    --ink-soft: #3d6770;
    --paper: #fbfbfa;
    --backdrop: #dcd9d4;
    --pattern: #e7ebec;
  }
  * { margin: 0; padding: 0; box-sizing: border-box; }
  html, body { width: 1200px; height: 544px; overflow: hidden; }
  body {
    background: var(--backdrop);
    font-family: "Alegreya", Georgia, serif;
    color: var(--ink);
    position: relative;
  }
  .specials-page {
    position: absolute;
    left: 413px; top: 12px;
    width: 373px; height: 520px;
    background: var(--paper);
    border-radius: 12px;
    overflow: hidden;
  }
  .pattern-area {
    position: absolute;
    right: 0; top: 0;
    width: 170px; height: 160px;
    background: radial-gradient(ellipse at top right, var(--pattern) 0%, rgba(231,235,236,0) 70%);
  }
  .pattern-area.bottom {
    left: 0; right: auto; top: auto; bottom: 0;
    width: 200px; height: 120px;
    background: radial-gradient(ellipse at bottom left, var(--pattern) 0%, rgba(231,235,236,0) 70%);
  }
  .cafe-name {
    position: absolute;
    left: 35px; top: 40px;
    width: 95px;
    font-weight: 900;
    font-size: 15px;
    line-height: 17px;
    text-align: center;
    text-transform: uppercase;
    letter-spacing: 0.5px;
  }
  .page-title {
    position: absolute;
    left: 36px; top: 441px;
    transform-origin: left top;
    transform: rotate(-90deg);
    font-size: 39px;
    font-weight: 400;
    line-height: 36px;
    letter-spacing: 0.5px;
    white-space: nowrap;
  }
  .divider {
    position: absolute;
    left: 82px; top: 96px;
    width: 1px; height: 343px;
    background: var(--ink);
  }
  .item { position: absolute; left: 91px; width: 240px; }
  .item-rule {
    position: absolute;
    left: 0; width: 80px; height: 1px;
    background: var(--ink);
  }
  .item-name {
    position: absolute; left: 39px;
    font-weight: 900; font-size: 11px;
    text-transform: uppercase; white-space: nowrap;
  }
  .item-category {
    position: absolute; left: 17px;
    font-size: 14px; white-space: nowrap;
    border-bottom: 1px solid var(--ink);
    line-height: 15px;
  }
  .item-desc {
    position: absolute; left: 39px;
    font-size: 8px; line-height: 12px;
    color: var(--ink-soft); white-space: nowrap;
  }
  .price {
    position: absolute; left: 220px;
    font-weight: 900; font-size: 11px;
  }
  .price sup { font-size: 6px; font-weight: 400; vertical-align: 5px; }
</style>
</head>
<body>
  <main class="specials-page">
    <div class="pattern-area" role="img" aria-label="Faint scattered splash pattern"></div>
    <div class="pattern-area bottom" role="img" aria-label="Faint scattered splash pattern"></div>

    <div class="cafe-name">Tallow Mill<br>Cafe</div>
    <h1 class="page-title">WEEKLY SPECIALS</h1>
    <div class="divider"></div>

    <section class="item" style="top:102px">
      <div class="item-rule" style="top:12px"></div>
      <h2 class="item-name" style="top:2px">Chicken Filo</h2>
      <p class="item-desc" style="top:17px">Creamy Chicken with Pinenuts, wrapped in Filo Pastry.<br>Served with Side Salad &amp; Zulu Sauce</p>
      <p class="price" style="top:45px"><sup>$</sup>24</p>
    </section>

    <section class="item" style="top:189px">
      <div class="item-rule" style="top:12px"></div>
      <h2 class="item-name" style="top:2px">Minestrone Soup</h2>
      <p class="item-desc" style="top:18px">Served with Garlic Bread</p>
      <p class="price" style="top:33px"><sup>$</sup>8</p>
    </section>

    <section class="item" style="top:262px">
      <h2 class="item-category" style="top:0">Cocktail Special</h2>
      <h3 class="item-name" style="top:21px">Passionista</h3>
      <p class="item-desc" style="top:36px">Vodka, Passionfruit Pulp, Mango Puree<br>Top up with Ginger &amp; Lemon Kombucha</p>
      <p class="price" style="top:62px"><sup>$</sup>17</p>
    </section>

    <section class="item" style="top:366px">
      <h2 class="item-category" style="top:0">Craft Beer Special</h2>
      <h3 class="item-name" style="top:22px">Sly Gecko</h3>
      <h3 class="item-name" style="top:40px">Sun Burst</h3>
      <p class="item-desc" style="top:58px">Tropical Pale Ale 4.8% Alc.</p>
      <p class="price" style="top:72px"><sup>$</sup>10</p>
    </section>
  </main>
</body>
</html>
```